Business card design Needed for new logo / Construction business, home extensions and new builds

We need a business card design using our new logo files which i will attach to this project :)

We are a small construction business specialising in home extensions, new builds and property development. We are very ambitious and would appreciate professional and elegant designs for our new business card.

Very serious about using the services on BriefNest and recently acquired our new logo from here :)

Please get involved, i will feedback when i can as i am very busy but can respond daily, thanks

Target Market(s)

People that want to build onto their houses, new building developments or adding too their existing property

Industry/Entity Type

Construction

Contact Information for Business Card

Hollin Marsh Construction, Tobias Renwick (Managing Director), Tel 07822200444, email - info@hollin-marsh, www.hollin-marsh.co.uk

Colors

Designer to choose colors to be used in the design.

Requirements
Must have
• I like a deep grey on the back please. A lot of you have provided black from and back, try mixing things up a little. The black looks cool 😎 Thanks

```html
<!DOCTYPE html>
<html lang="en">
<head>
<meta charset="utf-8">
<title>Hollin Marsh Construction – Business Cards</title>
<link href="https://fonts.googleapis.com/css2?family=Montserrat:wght@400;600;800&display=swap" rel="stylesheet">
<style>
  :root {
    --page-bg: #e4e4e2;
    --card-top: #1f1f1f;
    --card-bottom: #0c0c0c;
    --gold: #d9a427;
    --gold-deep: #b8861c;
    --silver: #c9c9c9;
    --muted: #a9a9a9;
    --icon-ink: #111111;
  }
  * { margin: 0; padding: 0; box-sizing: border-box; }
  html, body {
    width: 1200px; height: 846px; overflow: hidden;
    background: var(--page-bg);
    font-family: "Montserrat", sans-serif;
  }
  .stage { position: relative; width: 1200px; height: 846px; }

  .card {
    position: absolute;
    overflow: hidden;
    box-shadow: 6px 8px 14px rgba(0,0,0,0.22);
  }
  .card-texture {
    position: absolute; inset: 0;
    background: linear-gradient(170deg, var(--card-top) 0%, #191919 55%, var(--card-bottom) 100%);
  }
  .card-front { left: 183px; top: 169px; width: 292px; height: 509px; }
  .card-back  { left: 510px; top: 278px; width: 509px; height: 291px; }
  .card-back .card-texture {
    background: linear-gradient(100deg, #262626 0%, #1c1c1c 60%, #0e0e0e 100%);
  }

  .brand {
    position: absolute; left: 0; right: 0;
    display: flex; flex-direction: column; align-items: center;
    color: var(--gold);
    font-weight: 600;
    text-transform: uppercase;
    text-align: center;
  }
  .brand-square { background: var(--gold); }
  .card-front .brand { top: 82px; }
  .card-front .brand-square { width: 22px; height: 22px; margin-bottom: 22px; }
  .card-front .brand-name { font-size: 19px; letter-spacing: 1px; line-height: 1.25; }

  .card-back .brand { top: 70px; }
  .card-back .brand-square { width: 32px; height: 32px; margin-bottom: 30px; }
  .card-back .brand-name { font-size: 28px; letter-spacing: 1.5px; line-height: 1.25; }

  .person { position: absolute; left: 0; right: 0; top: 258px; text-align: center; }
  .person-name { color: var(--gold); font-weight: 800; font-size: 21px; letter-spacing: 0.3px; }
  .person-role { color: var(--muted); font-size: 15px; margin-top: 1px; }

  .contact-icons { position: absolute; left: 39px; width: 213px; top: 319px; height: 33px; }
  .contact-icons .rule {
    position: absolute; left: 0; right: 0; top: 16px; height: 1px; background: var(--gold-deep);
  }
  .icon-box {
    position: absolute; top: 0; width: 34px; height: 33px;
    background: var(--gold);
    display: flex; align-items: center; justify-content: center;
  }
  .icon-box svg { width: 22px; height: 22px; }

  .contact { position: absolute; left: 0; right: 0; text-align: center; }
  .contact-phone { top: 363px; color: var(--gold); font-weight: 800; font-size: 27px; letter-spacing: 0.5px; }
  .contact-email { top: 396px; color: var(--muted); font-size: 15px; }
  .contact-web { top: 418px; color: var(--muted); font-size: 15px; }
</style>
</head>
<body>
<main class="stage">

  <section class="card card-front">
    <div class="card-texture" role="img" aria-label="Dark abstract layered shape texture"></div>

    <div class="brand">
      <span class="brand-square"></span>
      <span class="brand-name">Hollin Marsh<br>Construction</span>
    </div>

    <div class="person">
      <p class="person-name">Tobias Renwick</p>
      <p class="person-role">Managing Director</p>
    </div>

    <div class="contact-icons">
      <span class="rule"></span>
      <span class="icon-box" style="left:30px" aria-label="Phone">
        <svg viewBox="0 0 24 24"><path fill="var(--icon-ink)" d="M6.6 2.5l3 3.3-1.8 2.4c1 2.3 2.9 4.4 5.6 5.9l2.3-1.9 3.4 3-1.6 3.2c-.4.6-1.1.9-1.8.7C9 17.4 4.7 12.4 3.4 5.5c-.1-.7.2-1.4.8-1.7z"/></svg>
      </span>
      <span class="icon-box" style="left:89px" aria-label="Email">
        <svg viewBox="0 0 24 24" fill="none" stroke="var(--icon-ink)" stroke-width="1.4"><rect x="2" y="5" width="20" height="14"/><path d="M2 5l10 8 10-8M2 19l7.5-7M22 19l-7.5-7"/></svg>
      </span>
      <span class="icon-box" style="left:148px" aria-label="Website">
        <svg viewBox="0 0 24 24" fill="none" stroke="var(--icon-ink)" stroke-width="1.4"><circle cx="12" cy="12" r="9.5"/><ellipse cx="12" cy="12" rx="4.5" ry="9.5"/><path d="M12 2.5v19M2.5 12h19M4 7h16M4 17h16"/></svg>
      </span>
    </div>

    <p class="contact contact-phone">07822 200 444</p>
    <p class="contact contact-email">info@hollin-marsh.co.uk</p>
    <p class="contact contact-web">www.hollin-marsh.co.uk</p>
  </section>

  <section class="card card-back">
    <div class="card-texture" role="img" aria-label="Deep grey abstract layered shape texture"></div>
    <div class="brand">
      <span class="brand-square"></span>
      <span class="brand-name">Hollin Marsh<br>Construction</span>
    </div>
  </section>

</main>
</body>
</html>
```